Flyer for annual KESTREL SUMMIT 2020

I would like a church event flyer designed. The event is called "KESTREL SUMMIT 2020". I am looking for a professional, yet catchy design that uses our brand colors and logo creatively while communicating key information of the event effectively.

1. The logo is attached in two color formats. The designer has the choice to use them as he/she want.

2. The location of the event is: Harlow Community Center, 239 Fennimore Street, Portland, ME 04117

3. Time and date of event. The designer can organize and format the date and time as he/she pleases.
Thursday December 31st @ 6:30PM
Friday January 1st @ 6:30PM
Saturday 2nd @ 6:30PM
Sunday 3rd @ 4:30PM

4. The topic of the event is "In Fire and On Fire". The designer is free to use this phrase as he/she pleases to create a good composition.

5. Speaker: Prophet Marcus Olunde (2 pictures of the speaker to choose from are attached)

6. Contact information: contact@brightmeadowfold.org - Telephone number: 207 583 2914

7. I would also like the following three words on the flyer. These words describe the focus of the event: FIRE, REVIVAL, PROPHETIC

Target Market(s)

Young adults

Font styles to use
Sans Serif

Requirements
Must have
• Logo, speaker's picture
Should not have
• cross image, church image

```html
<!DOCTYPE html>
<html lang="en">
<head>
<meta charset="utf-8">
<title>Kestrel Summit 2020 Flyer</title>
<link href="https://fonts.googleapis.com/css2?family=Montserrat:wght@500;600;700;800;900&display=swap" rel="stylesheet">
<style>
  :root {
    --backdrop: #3b2418;
    --flame-dark: #8a1f08;
    --flame-deep: #c2410c;
    --flame-mid: #f26a1b;
    --flame-light: #f9a531;
    --flame-glow: #ffd36a;
    --gold: #f5b41c;
    --yellow: #ffd21f;
    --navy: #1c3478;
    --blue: #2b4f9e;
    --orange: #f07a1a;
    --white: #ffffff;
    --suit-red: #c9341c;
  }
  * { box-sizing: border-box; margin: 0; padding: 0; }
  html, body { width: 1200px; height: 800px; overflow: hidden; }
  body {
    background: var(--backdrop);
    font-family: "Montserrat", sans-serif;
    position: relative;
  }
  .flyer {
    position: absolute;
    left: 317px; top: 0;
    width: 566px; height: 800px;
    background: var(--white);
    overflow: hidden;
  }
  .hero-photo {
    position: absolute; left: 0; top: 0; width: 566px; height: 480px;
    background:
      radial-gradient(ellipse 38% 30% at 78% 78%, var(--flame-glow) 0%, var(--flame-light) 35%, transparent 75%),
      radial-gradient(ellipse 30% 22% at 55% 85%, var(--flame-light) 0%, transparent 70%),
      radial-gradient(ellipse 45% 35% at 80% 35%, var(--flame-dark) 0%, transparent 70%),
      radial-gradient(ellipse 40% 40% at 15% 20%, var(--flame-light) 0%, transparent 70%),
      linear-gradient(160deg, var(--flame-mid) 0%, var(--flame-deep) 55%, var(--flame-mid) 100%);
  }
  .shapes { position: absolute; left: 0; top: 0; }
  .speaker-photo {
    position: absolute; left: 0; top: 470px; width: 200px; height: 330px;
    background: linear-gradient(180deg, #6b2a1a 0%, var(--suit-red) 45%, #a3260f 100%);
  }
  .frame {
    position: absolute; left: 16px; top: 16px; right: 16px; bottom: 16px;
    border: 2px solid var(--gold);
    pointer-events: none;
  }
  .event-name {
    position: absolute; left: 40px; top: 34px; width: 490px;
    color: var(--gold); font-weight: 600; font-size: 17px;
    letter-spacing: 7px; text-align: right;
  }
  .topic {
    position: absolute; left: 40px; top: 70px;
    font-weight: 900; font-size: 58px; line-height: 0.92;
    letter-spacing: -2px; color: var(--white); text-transform: uppercase;
  }
  .topic .accent { color: var(--yellow); }
  .brand {
    position: absolute; left: 40px; top: 360px;
    display: flex; align-items: center; gap: 8px;
    color: var(--white); font-weight: 700; font-size: 30px; letter-spacing: 1px;
  }
  .brand-dot { width: 12px; height: 12px; border-radius: 50%; background: var(--orange); }
  .session {
    position: absolute; width: 168px; height: 44px;
    background: var(--navy); color: var(--white);
    padding: 5px 10px; line-height: 1.1;
  }
  .session .day { font-size: 11px; font-weight: 600; display: block; }
  .session .time { font-size: 16px; font-weight: 700; display: block; text-align: right; }
  .s1 { left: 212px; top: 490px; }
  .s2 { left: 212px; top: 542px; }
  .s3 { left: 384px; top: 508px; }
  .s4 { left: 384px; top: 560px; }
  .speaker {
    position: absolute; left: 214px; top: 604px;
    text-transform: uppercase; line-height: 1.05;
  }
  .speaker .label { color: var(--navy); font-weight: 900; font-size: 24px; letter-spacing: 1px; }
  .speaker .name { color: var(--orange); font-weight: 800; font-size: 15px; }
  .venue {
    position: absolute; left: 382px; top: 616px; width: 162px;
    color: var(--navy); text-transform: uppercase; line-height: 1.1; text-align: center;
  }
  .venue .place { font-weight: 900; font-size: 19px; }
  .venue .place-sub { font-weight: 800; font-size: 12px; display: block; }
  .venue .address { font-weight: 700; font-size: 10px; display: block; margin-top: 3px; }
  .contact {
    position: absolute; left: 312px; top: 698px; width: 240px;
    color: var(--orange); text-align: center;
  }
  .contact .phone {
    display: flex; align-items: center; justify-content: center; gap: 6px;
    font-weight: 800; font-size: 25px; letter-spacing: 2px; white-space: nowrap;
  }
  .contact .email {
    display: flex; align-items: center; justify-content: center; gap: 5px;
    font-weight: 700; font-size: 9px; letter-spacing: 1.2px; text-transform: uppercase;
    margin-top: 3px; white-space: nowrap;
  }
  .base-band { position: absolute; left: 0; bottom: 0; width: 566px; height: 26px; background: var(--navy); }
</style>
</head>
<body>
  <main class="flyer">
    <div class="hero-photo" role="img" aria-label="Photo of a crowd surrounded by flames in warm orange tones"></div>

    <svg class="shapes" width="566" height="800" viewBox="0 0 566 800" aria-hidden="true">
      <polygon points="0,300 300,470 0,470" fill="var(--blue)"/>
      <polygon points="0,470 300,470 566,400 566,470" fill="var(--navy)"/>
      <polygon points="260,470 566,440 566,470" fill="var(--orange)"/>
      <polygon points="0,470 566,470 566,800 0,800" fill="var(--white)"/>
      <polygon points="200,690 300,690 282,774 200,774" fill="var(--blue)"/>
    </svg>

    <div class="speaker-photo" role="img" aria-label="Portrait of the speaker in a red suit and glasses"></div>

    <div class="base-band"></div>
    <div class="frame"></div>

    <p class="event-name">KESTREL SUMMIT 2020</p>
    <h1 class="topic">In Fire<br>And<br><span class="accent">On Fire</span></h1>

    <div class="brand"><span class="brand-dot"></span>VOXARA</div>

    <div class="session s1"><span class="day">Thursday December 31st</span><span class="time">@ 6:30PM</span></div>
    <div class="session s2"><span class="day">Saturday 2nd</span><span class="time">@ 6:30PM</span></div>
    <div class="session s3"><span class="day">Friday January 1st</span><span class="time">@ 6:30PM</span></div>
    <div class="session s4"><span class="day">Sunday 3rd</span><span class="time">@ 4:30PM</span></div>

    <div class="speaker">
      <div class="label">Speaker:</div>
      <div class="name">Prophet<br>Marcus Olunde</div>
    </div>

    <div class="venue">
      <div class="place">Harlow</div>
      <span class="place-sub">Community Center,</span>
      <span class="address">239 Fennimore Street,<br>Portland, ME 04117.</span>
    </div>

    <div class="contact">
      <div class="phone">
        <svg width="16" height="20" viewBox="0 0 18 22" aria-hidden="true"><path d="M5 1 L1 4 C0 9 4 17 11 21 L15 18 L11 14 L8 16 C6 13 5 10 5 8 L8 6 Z" fill="var(--orange)"/></svg>
        207 583 2914
      </div>
      <div class="email">
        <svg width="12" height="9" viewBox="0 0 12 9" aria-hidden="true"><rect x="0.5" y="0.5" width="11" height="8" fill="var(--orange)"/><path d="M0.5 0.5 L6 5 L11.5 0.5" stroke="#fff" fill="none"/></svg>
        contact@brightmeadowfold.org
      </div>
    </div>
  </main>
</body>
</html>
```